Create a Landing Page Design

I need a landing page designed and coded in HTML for tallfern.com that follows an "F" pattern design.

Examples:

Quillbarrow: https://www.quillbarrow.example/form/sem/sales_software.jsp?d=48260000000tkP7&DCMP=KNC-Search&mkwid=R8wq2Lm5&pcrid=58204917362&type=Exact&pdv=c&nc=48260000000mbHQ&gclid=DKoRn47f2M1DGfSmPhpeRHxBkR
Jug: https://app.jug.example/signup/o/sendlargefiles?kw=jug%20cloud%20storage&gclid=DJaLrfnf2M1DGT2fPhpe1GNBOR
Cobaltwick: http://www.cobaltwick.example/Landing-Templates/Search-Demo/?Reach_Campaign_ID=48270000000Jtwu&Reach_Campaign_Status=Registered&LeadSource=OnlineDemo_Search_48270000000Jtwu&PromoCode=OnlineDemo_Search_48270000000Jtwu&gclid=DJD1pL7g2M1DGZziPhpePH5B6R
Plumtide: http://pages2.plumtide.example/PPC-MarketingAutomationforLife.html?source=PPC&comment=PPC_GS_US&ag=Competition%20-%20Norvane&camp=Competition%20Marketing%20Automation&_kk=52542849458&kw=norvane&gclid=DMzSmKPg2M1DGX6fPhpeQycBLB
Gladwell Helper: http://gladwellhelper.example/free-helpdesk-software?gclid=DKQFovjg2M1DGfxEPhpegNB1h
Pult: http://help.pult.example/free-trial?source1=Adverts-CPC-Freetrial-BramlineNA&pi_ad_id=59602686359&gclid=DQ_ftf3g2M1DGf18PhpeilJBvB

It needs:

- Bullet point content to the left
- Sign-up form to the right (with image) - we'll provide the code for this
- Testimonials underneath
- A "human" image that conveys that there are people behind the brand. Here's a link to a filecrate folder of stock images we've purchased on this theme: https://www.filecrate.example/sh/uz1fbp5upmj0nvy/q5hL7VVvl8

I've attached a simple SketchRill wireframe so you understand what we're looking for.

We'd like to use our existing (https://tallfern.com/) header and footer, but remove all links (other than privacy policy + terms of service).

Thanks!

```html
<!DOCTYPE html>
<html lang="en">
<head>
<meta charset="utf-8">
<title>Tallfern – Simplify How You Work with Freelancers</title>
<link rel="stylesheet" href="https://fonts.googleapis.com/css2?family=Tinos&family=Arimo:wght@400&family=Open+Sans:wght@700&display=swap">
<style>
  :root {
    --white: #ffffff;
    --ink: #333333;
    --logo-grey: #6b6b6b;
    --logo-dot: #f0962a;
    --hero-dark: #5a5a5a;
    --hero-mid: #8e8e8e;
    --hero-light: #c9c9c9;
    --panel-dark: rgba(62, 62, 62, 0.9);
    --strip-dark: #2d2d2d;
    --panel-light: rgba(218, 218, 218, 0.95);
    --orange: #f0962a;
    --muted: #b9b9b9;
    --bullet-head: #bdbdbd;
    --submit: #4a6b97;
    --link-blue: #3e6590;
    --navy: #22267a;
    --black: #000000;
  }
  * { box-sizing: border-box; margin: 0; padding: 0; }
  html, body { width: 1200px; height: 961px; overflow: hidden; background: var(--white); }
  body { position: relative; font-family: "Tinos", serif; color: var(--ink); }

  .site-header { position: absolute; left: 0; top: 0; width: 1200px; height: 145px; background: var(--white); }
  .brand { position: absolute; left: 40px; top: 38px; display: flex; align-items: center; gap: 18px; }
  .brand-dot { width: 72px; height: 72px; border-radius: 50%; background: var(--logo-dot); }
  .brand-name { font-family: "Arimo", sans-serif; font-size: 34px; color: var(--logo-grey); }
  .main-nav { position: absolute; top: 52px; right: 39px; display: flex; gap: 60px; }
  .main-nav a { font-size: 24px; color: var(--ink); text-decoration: none; }

  .hero { position: absolute; left: 0; top: 145px; width: 1200px; height: 614px; }
  .hero-photo { position: absolute; inset: 0;
    background: linear-gradient(180deg, var(--hero-dark) 0%, var(--hero-mid) 45%, var(--hero-light) 70%, var(--hero-mid) 100%); }

  .pitch { position: absolute; left: 36px; top: 36px; width: 546px; height: 542px; background: var(--panel-dark); }
  .pitch-title { position: absolute; left: 36px; top: 34px; font-size: 29px; font-weight: 400; color: var(--white); white-space: nowrap; }
  .pitch-sub { position: absolute; left: 36px; top: 70px; font-size: 20px; line-height: 27px; color: var(--muted); }
  .pitch-offer { position: absolute; left: 36px; top: 143px; font-size: 20px; line-height: 27px; color: var(--orange); }
  .bullet-strip { position: absolute; left: 0; top: 237px; width: 54px; height: 305px; background: var(--strip-dark); }
  .benefits { position: absolute; left: 0; top: 243px; list-style: none; }
  .benefit { position: relative; height: 102px; padding-left: 83px; font-family: "Arimo", sans-serif; font-size: 14.5px; line-height: 18px; }
  .benefit-arrow { position: absolute; left: 36px; top: 8px; width: 30px; height: 34px; }
  .benefit-head { color: var(--bullet-head); text-transform: uppercase; }
  .benefit-text { color: var(--white); }

  .pointer { position: absolute; left: 571px; top: 73px; width: 58px; height: 65px; }

  .signup { position: absolute; left: 618px; top: 36px; width: 546px; height: 542px; background: var(--panel-light); }
  .signup-intro { position: absolute; left: 88px; top: 40px; font-size: 17px; line-height: 23px; color: var(--black); }
  .signup-field { position: absolute; left: 88px; width: 376px; height: 46px; border: 0; background: var(--white); }
  .field-1 { top: 131px; } .field-2 { top: 185px; } .field-3 { top: 239px; }
  .signup-submit { position: absolute; left: 88px; top: 333px; width: 376px; height: 46px; border: 0;
    background: var(--submit); color: var(--white); font-family: "Arimo", sans-serif; font-size: 19px; }
  .privacy { position: absolute; left: 88px; top: 417px; width: 190px; font-family: "Arimo", sans-serif;
    font-size: 14.5px; line-height: 17px; color: var(--link-blue); text-decoration: none; }

  .clients { position: absolute; left: 0; top: 759px; width: 1200px; height: 143px; background: var(--white); }
  .client { position: absolute; top: 35px; height: 73px; background: var(--navy); color: var(--white);
    font-family: "Open Sans", sans-serif; font-weight: 700; font-size: 21px; line-height: 73px; padding-left: 22px; }
  .client-1 { left: 35px; width: 249px; } .client-2 { left: 323px; width: 257px; padding-left: 34px; }
  .client-3 { left: 618px; width: 264px; } .client-4 { left: 922px; width: 242px; padding-left: 26px; }

  .site-footer { position: absolute; left: 0; top: 902px; width: 1200px; height: 59px; background: var(--black);
    color: var(--white); font-family: "Open Sans", sans-serif; font-weight: 700; font-size: 11px; line-height: 59px; text-align: center; }
</style>
</head>
<body>
  <header class="site-header">
    <div class="brand"><span class="brand-dot"></span><span class="brand-name">Tallfern</span></div>
    <nav class="main-nav">
      <a href="#">Join Now</a>
      <a href="#">TallfernBlog</a>
      <a href="#">Login</a>
    </nav>
  </header>

  <main class="hero">
    <div class="hero-photo" role="img" aria-label="Soft-focus photo of a crowd of people walking across a wide open plaza"></div>

    <section class="pitch">
      <h1 class="pitch-title">Simplify How You Work with Freelancers,</h1>
      <p class="pitch-sub">Instantly access 10 million qualified workers<br>from within the apps you love.</p>
      <p class="pitch-offer">Post any Task or Search<br>for a Worker for Free.</p>
      <div class="bullet-strip"></div>
      <ul class="benefits">
        <li class="benefit">
          <svg class="benefit-arrow" viewBox="0 0 30 34"><polyline points="4,4 26,17 4,30" fill="none" stroke="#f0962a" stroke-width="5"/></svg>
          <div class="benefit-head">These are benefit-level bullets crafted for skimmers</div>
          <div class="benefit-text">The benefit goes a bit deeper into the benefit above.</div>
        </li>
        <li class="benefit">
          <svg class="benefit-arrow" viewBox="0 0 30 34"><polyline points="4,4 26,17 4,30" fill="none" stroke="#f0962a" stroke-width="5"/></svg>
          <div class="benefit-head">These are benefit-level bullets crafted for skimmers</div>
          <div class="benefit-text">The benefit goes a bit deeper into the benefit above.</div>
        </li>
        <li class="benefit">
          <svg class="benefit-arrow" viewBox="0 0 30 34"><polyline points="4,4 26,17 4,30" fill="none" stroke="#f0962a" stroke-width="5"/></svg>
          <div class="benefit-head">These are benefit-level bullets crafted for skimmers</div>
          <div class="benefit-text">The benefit goes a bit deeper into the benefit above.</div>
        </li>
      </ul>
    </section>

    <svg class="pointer" viewBox="0 0 58 65"><polygon points="0,0 58,32.5 0,65" fill="#f0962a"/></svg>

    <section class="signup">
      <p class="signup-intro">Some text here<br>regarding the form.</p>
      <input class="signup-field field-1" type="text" aria-label="Field one">
      <input class="signup-field field-2" type="text" aria-label="Field two">
      <input class="signup-field field-3" type="text" aria-label="Field three">
      <button class="signup-submit" type="button">SUBMIT</button>
      <a class="privacy" href="#">Privacy policy descriptions here</a>
    </section>
  </main>

  <section class="clients">
    <div class="client client-1">ICONS</div>
    <div class="client client-2">OF</div>
    <div class="client client-3">USER</div>
    <div class="client client-4">COMPANIES</div>
  </section>

  <footer class="site-footer">Copyright : etc.</footer>
</body>
</html>
```